Meridale Tax Advisers Business Card

We are seeking a clean, professional, and modern double sided business card design for Meridale Tax Advisers, a tax, accounting, and advisory firm serving business owners, professionals, and investors.
The design should convey credibility, precision, trust, and sophistication appropriate for a CPA level tax advisory firm. Avoid playful, trendy, or overly decorative styles. The look should be sharp, balanced, and timeless.
Our official company logo has been uploaded, which must be incorporated appropriately and consistently with the brand. Designers should not modify, distort, or recreate the logo.
Card format
Standard US business card size (3.5 x 2 inches)
Double sided
Design direction
Professional and modern
Minimalist and uncluttered
Strong typography and clean spacing
Subtle visual interest is welcome, but simplicity is preferred
High contrast and readability are critical
Front side
Primary focus on the Meridale Tax Advisers logo
The firm name should be clearly legible and visually prominent
Background may be white or dark, depending on what best complements the logo
Back side
Contact information layout, such as
Name: Peter L. Garnick, MSA, CFP®, AIF®, EA
Title: Managing Director, Tax
Email: pgarnick@mymeridale.example
Website: https://www.meridale.example/
Mobile: (555) 318-2047
Direct: (555) 642-7130
Main: (555) 642-7188
Address: 2870 Fenwick Rd., Suite 415, Larkmoor, TX 00000
Icons may be used sparingly if they enhance clarity
The layout should feel organized and structured
Color and style
Use colors that complement the uploaded logo
Neutral, professional tones preferred
Avoid loud or saturated colors
The design should print well on standard cardstock
Print considerations
Design should be print‑ready
No edge to edge elements that risk being cut off
Proper margins and bleed awareness
Overall, the goal is a polished, high end business card that reflects trust, expertise, and professionalism consistent with a firm providing tax strategy, compliance, and advisory services.

```html
<!DOCTYPE html>
<html lang="en">
<head>
<meta charset="utf-8">
<title>Meridale Tax Advisers – Business Card</title>
<link href="https://fonts.googleapis.com/css2?family=Inter:wght@300;400;500;600;700&display=swap" rel="stylesheet">
<style>
:root{
  --stage:#1d1d1e;
  --card:#262627;
  --card-deep:#202021;
  --frame:#8f9197;
  --copper-light:#e9a476;
  --copper:#c97a4a;
  --copper-dark:#9a5530;
  --silver-light:#e4e5e8;
  --silver:#a9abb0;
  --ink:#ececee;
  --ink-soft:#bfc1c6;
  --label:#8a8b8f;
  --brand:#d3d5db;
  --accent:#d68552;
}
*{box-sizing:border-box;margin:0;padding:0}
html,body{width:1200px;height:896px;overflow:hidden}
body{background:var(--stage);font-family:"Inter",sans-serif;position:relative}
.side-label{position:absolute;top:118px;width:465px;text-align:center;font-size:21px;font-weight:400;color:var(--label)}
.card{position:absolute;width:465px;height:263px;background:var(--card);overflow:hidden}
.card__frame{position:absolute;inset:13px 12px;border:2px solid var(--frame)}
.card__texture{position:absolute;inset:15px 14px;background:
  radial-gradient(ellipse at 85% 30%,rgba(255,255,255,.05),transparent 55%),
  radial-gradient(ellipse at 15% 85%,rgba(0,0,0,.25),transparent 60%),
  linear-gradient(160deg,var(--card) 0%,var(--card-deep) 100%)}
.tab{position:absolute}
.tab--copper{background:linear-gradient(90deg,var(--copper-dark),var(--copper-light) 50%,var(--copper-dark))}
.tab--silver{background:linear-gradient(180deg,var(--silver),var(--silver-light) 50%,var(--silver))}
.tab--top{top:0;left:155px;width:155px;height:12px;border-radius:0 0 10px 10px}
.tab--bottom{bottom:0;left:155px;width:155px;height:12px;border-radius:10px 10px 0 0}
.tab--left{left:0;top:78px;width:10px;height:110px;border-radius:0 10px 10px 0}
.tab--right{right:0;top:78px;width:10px;height:110px;border-radius:10px 0 0 10px}
.tab--left.tab--copper,.tab--right.tab--copper{background:linear-gradient(180deg,var(--copper-dark),var(--copper-light) 50%,var(--copper-dark))}

.brand{position:absolute;left:88px;top:94px;display:flex;align-items:center;gap:16px}
.brand__mark{width:44px;height:44px;border-radius:50%;background:var(--copper)}
.brand__name{color:var(--brand);font-weight:500;line-height:1}
.brand__primary{display:block;font-size:40px;letter-spacing:2px}
.brand__secondary{display:block;font-size:25px;letter-spacing:3.2px;margin-top:8px}

.contact{position:absolute;left:44px;color:var(--ink)}
.contact__name{font-size:20px;font-weight:700;color:var(--ink);white-space:nowrap}
.contact__creds{font-size:16px;font-weight:500}
.contact__title{font-size:15px;color:var(--ink-soft);margin-top:2px}
.contact__list{list-style:none;font-size:15px;line-height:18.5px}
.contact__row{display:flex;gap:13px;align-items:flex-start;white-space:nowrap}
.contact__icon{width:14px;height:14px;flex:none;margin-top:2px}
.contact__group{margin-top:6px}
</style>
</head>
<body>

<p class="side-label" style="left:120px">Front Card</p>
<p class="side-label" style="left:620px">Back Card</p>

<section class="card card--front" style="left:110px;top:167px">
  <div class="card__texture" role="img" aria-label="Faint topographic contour lines and a rising candlestick chart"></div>
  <div class="card__frame"></div>
  <span class="tab tab--copper tab--top"></span>
  <span class="tab tab--copper tab--bottom"></span>
  <span class="tab tab--copper tab--left"></span>
  <span class="tab tab--copper tab--right"></span>
  <div class="brand">
    <span class="brand__mark"></span>
    <p class="brand__name"><span class="brand__primary">MERIDALE</span><span class="brand__secondary">Tax Advisers</span></p>
  </div>
</section>

<section class="card card--back" style="left:626px;top:167px">
  <div class="card__texture" role="img" aria-label="Faint rising candlestick chart"></div>
  <div class="card__frame"></div>
  <span class="tab tab--silver tab--left"></span>
  <span class="tab tab--silver tab--right"></span>
  <div class="contact" style="top:44px">
    <p class="contact__name">Peter L. Garnick<span class="contact__creds">, MSA, CFP®, AIF®, EA</span></p>
    <p class="contact__title">Managing Director, Tax</p>
    <ul class="contact__list" style="margin-top:21px">
      <li class="contact__row"><svg class="contact__icon" viewBox="0 0 14 14"><rect x="1" y="3" width="12" height="8.5" rx="1" fill="var(--accent)"/><path d="M1.5 3.5 7 8l5.5-4.5" stroke="var(--card)" stroke-width="1.2" fill="none"/></svg><span>pgarnick@mymeridale.example</span></li>
      <li class="contact__row"><svg class="contact__icon" viewBox="0 0 14 14" fill="none" stroke="var(--accent)" stroke-width="1.2"><circle cx="7" cy="7" r="5.5"/><ellipse cx="7" cy="7" rx="2.3" ry="5.5"/><path d="M1.5 7h11"/></svg><span>https://www.meridale.example/</span></li>
      <li class="contact__row"><svg class="contact__icon" viewBox="0 0 14 14" fill="none" stroke="var(--accent)" stroke-width="1.3"><rect x="3.5" y="1" width="7" height="12" rx="1.2"/><path d="M6 11h2"/></svg><span>Mobile: (555) 318-2047<br>Direct: (555) 642-7130<br>Main: (555) 642-7188</span></li>
      <li class="contact__row"><svg class="contact__icon" viewBox="0 0 14 14"><path d="M7 13s4.5-4.6 4.5-7.6a4.5 4.5 0 0 0-9 0C2.5 8.4 7 13 7 13z" fill="var(--accent)"/><circle cx="7" cy="5.5" r="1.6" fill="var(--card)"/></svg><span>2870 Fenwick Rd., Suite 415, Larkmoor, TX 00000</span></li>
    </ul>
  </div>
</section>

<section class="card card--front" style="left:110px;top:478px">
  <div class="card__texture" role="img" aria-label="Faint topographic contour lines and a rising candlestick chart"></div>
  <div class="card__frame"></div>
  <span class="tab tab--copper tab--top"></span>
  <span class="tab tab--copper tab--bottom"></span>
  <span class="tab tab--copper tab--left"></span>
  <span class="tab tab--copper tab--right"></span>
  <div class="brand">
    <span class="brand__mark"></span>
    <p class="brand__name"><span class="brand__primary">MERIDALE</span><span class="brand__secondary">Tax Advisers</span></p>
  </div>
</section>

<section class="card card--back" style="left:626px;top:478px">
  <div class="card__texture" role="img" aria-label="Faint rising candlestick chart"></div>
  <div class="card__frame"></div>
  <span class="tab tab--silver tab--left"></span>
  <span class="tab tab--silver tab--right"></span>
  <div class="contact" style="top:32px">
    <p class="contact__name">Peter L. Garnick<span class="contact__creds">, MSA, CFP®, AIF®, EA</span></p>
    <p class="contact__title">Managing Director, Tax</p>
    <ul class="contact__list" style="margin-top:18px">
      <li class="contact__row"><svg class="contact__icon" viewBox="0 0 14 14"><rect x="1" y="3" width="12" height="8.5" rx="1" fill="var(--accent)"/><path d="M1.5 3.5 7 8l5.5-4.5" stroke="var(--card)" stroke-width="1.2" fill="none"/></svg><span>pgarnick@mymeridale.example</span></li>
      <li class="contact__row"><svg class="contact__icon" viewBox="0 0 14 14" fill="none" stroke="var(--accent)" stroke-width="1.2"><circle cx="7" cy="7" r="5.5"/><ellipse cx="7" cy="7" rx="2.3" ry="5.5"/><path d="M1.5 7h11"/></svg><span>https://www.meridale.example/</span></li>
      <li class="contact__row contact__group"><svg class="contact__icon" viewBox="0 0 14 14" fill="none" stroke="var(--accent)" stroke-width="1.3"><rect x="3.5" y="1" width="7" height="12" rx="1.2"/><path d="M6 11h2"/></svg><span>Mobile: (555) 318-2047<br>Direct: (555) 642-7130<br>Main: (555) 642-7188</span></li>
      <li class="contact__row contact__group"><svg class="contact__icon" viewBox="0 0 14 14"><path d="M7 13s4.5-4.6 4.5-7.6a4.5 4.5 0 0 0-9 0C2.5 8.4 7 13 7 13z" fill="var(--accent)"/><circle cx="7" cy="5.5" r="1.6" fill="var(--card)"/></svg><span>2870 Fenwick Rd., Suite 415,<br>Larkmoor, TX 00000</span></li>
    </ul>
  </div>
</section>

</body>
</html>
```